依頼詳細
・リスティングでの運用を考えているので、コンバージョンを期待できるデザイン、サイト構成
・レスポンシブでコーディングするためそれを念頭に置いたデザイン
・提案デザインはスマホ、PC両画面でお願いします。
・サイト構成も変わる可能性が高いので、HTMLやCSSでの変更が容易なデザイン
(メニューなどを画像にしないetc)
・奇抜さよりも安心感
・病院関係のウェブサイト構築実績のある方歓迎
・病院の場所はみなとみらいです。
ページ数
2ページ
希望イメージ
シンプル 複雑
単色 カラフル
暗い 明るい
日常 高級
遊び心 厳粛
未来的 伝統的
女性的 男性的
希望する色
青系、水色系、緑系、黄・オレンジ系
納品ファイル
• 高解像度JPG (.jpg)
• フォトショップ形式 (.psd)
補足説明
■ 補足
--------------------------------
・基本HTMLコーディングは無しで構いませんが、
対応可能な方はコーディング作業についてもお見積ください。

・採用された方は今後も引続き作業をお願いすることになると思います。

■ 注意点

・お渡しできる素材は、サイトマップのみとなります
・病院名なども決まっていないので、ロゴなどは仮のもので構いません。
・サイトの中の文言なども仮の文章で構いません。
・写真素材も仮のもので構いません。
(最終的には素材もしくは撮影した写真に入れ替えます。)

○想定サイトマップ
診療科目
病院案内
├ ご挨拶・理念
├ 施設案内
└ ドクター紹介
アクセス
よくある質問
採用情報
サイトマップ
お問い合わせ
予約

※サイト構成も決定ではないので提案頂く形でも構いません。

参考サイト
http://www.tokuro-dental.com/
https://www.clinic-mikura.com/
ウェブサイトの構成が、内科・整形外科・歯科の診療科目を一つのサイトで集患する形に変更になりました。大きい枠組みで変わるのはこれ以降はないと思います。素敵なデザイナー様との出会いを期待しております。
お盆に入ってしまうので、締切を延長させていただきました。今後も数々の案件抱えておりますので、長いお付き合いができるデザイナー様との出会いを期待しております。
たくさんのご応募、誠にありがとうございます!

これから社内で選定を行います。
一週間以内には決定できると思いますので少々お待ち頂ければと思います。
よろしくお願いいたします。
デザインの選定に時間がかかっておりますので、決定までもう少々お待ち頂ければと思います。申し訳ありません、よろしくお願いいたします。
■ 選んだ理由

シンプルにデザインがまとまっていたところと、アイコンなどを使いぱっと見た時のわかりやすさ、写真を変更しても違和感なくマッチしそうな点などを評価させていただきました。

■ 提案者全員のお礼・コメント

この度は弊社コンペにご参加頂き誠にありがとうございます。
優れたデザイン・提案を多数頂きとても感謝しております。

ギリギリまでどの提案を採用させていただくか迷いましたが、
今回はこのような結果となりました。

またの機会がありましたら、またぜひご参加頂ければ幸いです。
ありがとうございました。

```html
<!DOCTYPE html>
<html lang="ja">
<head>
<meta charset="utf-8">
<title>見本クリニック</title>
<link href="https://fonts.googleapis.com/css2?family=Noto+Sans+JP:wght@400;500;700&family=Noto+Serif+JP:wght@500;700&display=swap" rel="stylesheet">
<style>
:root{
  --brown:#6b4a2c;
  --brown-dark:#553a22;
  --teal:#46b3b1;
  --teal-light:#7fcfcb;
  --cream:#f6f1e8;
  --beige:#efe6d6;
  --text:#4a3b2e;
  --gray:#8a8178;
  --line:#ddd3c3;
  --white:#fff;
}
*{box-sizing:border-box;margin:0;padding:0}
html,body{width:1200px;height:3380px;overflow:hidden}
body{font-family:"Noto Sans JP",sans-serif;color:var(--text);background:var(--white);font-size:14px;line-height:1.7}
.serif{font-family:"Noto Serif JP",serif}
.photo{display:block}
/* header */
.site-header{height:200px;position:relative;padding:40px 60px 0}
.hours{border-collapse:collapse;font-size:12px;width:340px}
.hours th,.hours td{padding:3px 6px;text-align:center;border-bottom:1px dotted var(--line)}
.hours thead th{background:var(--brown);color:#fff;font-weight:500}
.hours td.dot{color:var(--brown)}
.hours .time{text-align:left;white-space:nowrap}
.hours-note{font-size:11px;color:var(--gray);margin-top:6px}
.brand{position:absolute;left:50%;top:38px;transform:translateX(-50%);text-align:center}
.brand-mark{width:60px;height:60px;border-radius:50%;background:var(--teal);margin:0 auto 8px}
.brand-name{font-size:26px;font-weight:700;color:var(--brown);letter-spacing:.08em}
.brand-sub{font-size:11px;color:var(--gray);letter-spacing:.2em}
.contact{position:absolute;right:60px;top:40px;display:flex;gap:8px}
.tels{display:flex;flex-direction:column;gap:6px}
.tel{display:flex;align-items:center;gap:8px;background:var(--teal);color:#fff;font-size:20px;font-weight:700;padding:4px 14px;width:230px}
.tel.brown{background:var(--brown)}
.reserve{background:var(--brown);color:#fff;font-size:18px;font-weight:700;width:70px;display:flex;align-items:center;justify-content:center;writing-mode:vertical-rl;letter-spacing:.3em}
.contact-label{position:absolute;right:60px;top:140px;font-size:10px;color:var(--gray);letter-spacing:.15em}
/* hero */
.hero{height:380px;position:relative;background:linear-gradient(180deg,#dfeef3,#eef3f2 60%,#d7e6d2)}
.hero-catch{position:absolute;left:120px;top:30px;writing-mode:vertical-rl;font-size:40px;font-weight:700;color:var(--brown);line-height:1.5;letter-spacing:.1em;background:rgba(255,255,255,.85);padding:24px 18px}
.hero-badge{position:absolute;right:70px;top:210px;width:140px;height:140px;border-radius:50%;background:var(--teal);border:4px solid #fff;color:#fff;font-size:13px;font-weight:700;display:flex;align-items:center;justify-content:center;text-align:center;line-height:1.5}
/* nav */
.global-nav{display:flex;justify-content:center;margin:30px auto 0;width:1020px;border-top:1px solid var(--line);border-bottom:1px solid var(--line)}
.global-nav a{flex:1;text-align:center;font-size:14px;color:var(--text);text-decoration:none;padding:18px 0;border-left:1px solid var(--line);display:flex;align-items:center;justify-content:center;gap:8px}
.global-nav a:last-child{border-right:1px solid var(--line)}
.global-nav svg{width:18px;height:18px}
/* news */
.news{width:1020px;margin:40px auto 0;display:flex;gap:40px;height:220px}
.news-title{width:180px;border-right:1px solid var(--line)}
.news-title h2{font-size:20px;color:var(--brown)}
.news-title span{font-size:10px;color:var(--gray);letter-spacing:.2em}
.news-list{list-style:none;flex:1}
.news-list li{display:flex;gap:24px;font-size:13px;padding:8px 0;border-bottom:1px dotted var(--line)}
.news-list time{color:var(--gray);width:90px}
.news-list a{color:var(--teal)}
/* about band */
.about{height:360px;margin-top:20px;position:relative;background:linear-gradient(90deg,var(--teal) 0 55%,var(--teal-light));color:#fff}
.about-body{position:absolute;left:90px;top:50px;width:540px}
.about h2{font-size:30px;line-height:1.5;font-weight:700;margin-bottom:20px}
.about p{font-size:13px;opacity:.95}
.btn-outline{display:inline-block;margin-top:24px;border:1px solid #fff;color:#fff;padding:8px 30px;border-radius:20px;font-size:13px}
.about-photo{position:absolute;right:0;top:0;width:520px;height:360px;background:linear-gradient(135deg,#a9dcd7,#e4f3f1)}
/* departments */
.departments{padding:60px 0 0;height:640px;text-align:center}
.section-title{font-size:22px;color:var(--brown);font-weight:700}
.section-title span{display:block;font-size:10px;color:var(--gray);letter-spacing:.3em;font-weight:400}
.dept-list{display:flex;justify-content:center;gap:40px;margin-top:40px}
.dept-card{width:300px;text-align:left}
.dept-card .photo{height:260px;background:linear-gradient(135deg,#e9f2f3,#c5dde1)}
.dept-card h3{text-align:center;font-size:20px;color:var(--brown);margin:18px 0 8px}
.dept-card p{font-size:12px;color:var(--gray)}
.btn-teal{display:block;width:170px;margin:18px auto 0;background:var(--teal);color:#fff;text-align:center;font-size:12px;padding:7px 0;border-radius:3px}
/* banners */
.banners{height:210px;background:var(--brown);display:flex;align-items:center;justify-content:center;gap:30px}
.banner{width:260px;height:100px;background:#fff;display:flex;align-items:center;gap:12px;padding:0 14px}
.banner .photo{width:110px;height:72px;background:linear-gradient(135deg,#d8ebe9,#f3ece0)}
.banner strong{font-size:16px;color:var(--brown)}
.gallery{display:flex;height:230px;margin-top:10px}
.gallery .photo{flex:1}
/* footer */
.site-footer{height:400px;background:var(--cream);position:relative;padding-top:30px}
.footer-brand{display:flex;align-items:center;justify-content:center;gap:14px}
.footer-brand .brand-mark{margin:0;width:56px;height:56px}
.footer-info{display:flex;justify-content:center;gap:40px;margin-top:30px}
.footer-address{font-size:12px;margin-bottom:14px}
.footer-address p{display:flex;gap:6px;align-items:center}
.footer-access{width:1020px;margin:20px auto 0;font-size:12px;color:var(--gray);line-height:1.8}
.footer-nav{display:flex;justify-content:center;gap:16px;font-size:12px;padding:20px 0;border-bottom:1px solid var(--line);width:1020px;margin:0 auto}
.map{height:460px;margin-top:30px;background:linear-gradient(135deg,#ece9e3,#dcdfd8 50%,#e8e4dc)}
.copyright{height:60px;background:var(--brown);color:#fff;font-size:11px;display:flex;align-items:center;justify-content:center;letter-spacing:.1em}
</style>
</head>
<body>
<header class="site-header">
  <table class="hours">
    <thead><tr><th>診療時間</th><th>月</th><th>火</th><th>水</th><th>木</th><th>金</th><th>土</th><th>日</th></tr></thead>
    <tbody>
      <tr><td class="time">9:00〜12:30</td><td class="dot">●</td><td class="dot">●</td><td class="dot">●</td><td class="dot">●</td><td class="dot">●</td><td class="dot">●</td><td>／</td></tr>
      <tr><td class="time">14:00〜18:00</td><td class="dot">●</td><td class="dot">●</td><td class="dot">●</td><td class="dot">●</td><td class="dot">●</td><td>▲</td><td>／</td></tr>
    </tbody>
  </table>
  <p class="hours-note">休診日：日曜・祝日　▲土曜午後は17:00まで</p>
  <div class="brand">
    <div class="brand-mark"></div>
    <div class="brand-name">見本クリニック</div>
    <div class="brand-sub">内科・整形外科・歯科</div>
  </div>
  <div class="contact">
    <div class="tels">
      <div class="tel"><svg width="18" height="18" viewBox="0 0 24 24" fill="#fff"><path d="M6.6 10.8a15 15 0 0 0 6.6 6.6l2.2-2.2a1 1 0 0 1 1-.25 11.4 11.4 0 0 0 3.6.57 1 1 0 0 1 1 1V20a1 1 0 0 1-1 1A17 17 0 0 1 3 4a1 1 0 0 1 1-1h3.5a1 1 0 0 1 1 1c0 1.25.2 2.45.57 3.6a1 1 0 0 1-.25 1z"/></svg>010-234-5678</div>
      <div class="tel brown"><svg width="18" height="18" viewBox="0 0 24 24" fill="#fff"><path d="M6.6 10.8a15 15 0 0 0 6.6 6.6l2.2-2.2a1 1 0 0 1 1-.25 11.4 11.4 0 0 0 3.6.57 1 1 0 0 1 1 1V20a1 1 0 0 1-1 1A17 17 0 0 1 3 4a1 1 0 0 1 1-1h3.5a1 1 0 0 1 1 1c0 1.25.2 2.45.57 3.6a1 1 0 0 1-.25 1z"/></svg>010-234-5678</div>
    </div>
    <div class="reserve">予約</div>
  </div>
  <div class="contact-label">RESERVATION &amp; CONTACT</div>
</header>

<section class="hero">
  <div class="photo" role="img" aria-label="白い外壁のクリニック外観と青空" style="position:absolute;inset:0;background:linear-gradient(180deg,#d9ecf4,#f1f3f0 55%,#c9dcc3)"></div>
  <h1 class="hero-catch serif">キャッチコピー<br>アピールポイントが<br>入ります。</h1>
  <div class="hero-badge">駅から徒歩3分<br>土曜日も<br>午前診療</div>
</section>

<nav class="global-nav">
  <a href="#">HOME</a>
  <a href="#"><svg viewBox="0 0 24 24" fill="none" stroke="#6b4a2c" stroke-width="2"><rect x="4" y="4" width="16" height="16" rx="2"/><path d="M12 8v8M8 12h8"/></svg>病院案内</a>
  <a href="#"><svg viewBox="0 0 24 24" fill="none" stroke="#6b4a2c" stroke-width="2"><circle cx="12" cy="12" r="8"/><path d="M12 8v8M8 12h8"/></svg>診療科目</a>
  <a href="#"><svg viewBox="0 0 24 24" fill="none" stroke="#6b4a2c" stroke-width="2"><path d="M12 21s-6-6-6-11a6 6 0 0 1 12 0c0 5-6 11-6 11z"/><circle cx="12" cy="10" r="2"/></svg>アクセス</a>
  <a href="#"><svg viewBox="0 0 24 24" fill="none" stroke="#6b4a2c" stroke-width="2"><circle cx="12" cy="12" r="9"/><path d="M9.5 9.5a2.5 2.5 0 1 1 3.5 2.3c-.6.3-1 .9-1 1.5V14M12 17h.01"/></svg>よくある質問</a>
  <a href="#"><svg viewBox="0 0 24 24" fill="none" stroke="#6b4a2c" stroke-width="2"><circle cx="12" cy="8" r="4"/><path d="M4 21c0-4 4-6 8-6s8 2 8 6"/></svg>採用情報</a>
</nav>

<section class="news">
  <div class="news-title"><h2>お知らせ</h2><span>NEWS</span></div>
  <ul class="news-list">
    <li><time>2017.08.24</time>夏季休診のお知らせを掲載しております。<a href="#">詳しくはこちら</a></li>
    <li><time>2017.08.10</time>見本クリニックのホームページを公開しました。よろしくお願いします。</li>
    <li><time>2017.08.01</time>見本クリニックからのお知らせ文が入ります。サンプルテキストです。</li>
    <li><time>2017.07.20</time>見本クリニックからのお知らせ文が入ります。サンプルテキストです。</li>
  </ul>
</section>

<section class="about">
  <div class="about-photo photo" role="img" aria-label="白衣の医師が診察室で微笑む写真"></div>
  <div class="about-body">
    <h2 class="serif">整形外科・歯科・総合内科専門医として<br>〇〇市の皆様から信頼される、頼りにされる病院を。</h2>
    <p>こちらにクリニックの理念や診療方針についての紹介文が入ります。地域の皆様に安心して通っていただけるよう、丁寧な診療と分かりやすい説明を心がけております。こちらは仮の文章です。</p>
    <span class="btn-outline">ご挨拶・理念はこちら　›</span>
  </div>
</section>

<section class="departments">
  <h2 class="section-title">診療科目<span>MEDICAL</span></h2>
  <div class="dept-list">
    <article class="dept-card">
      <div class="photo" role="img" aria-label="レントゲン画像を確認する医師"></div>
      <h3>整形外科</h3>
      <p>整形外科についての簡単な紹介文が入ります。骨や関節、筋肉の痛みなどお気軽にご相談ください。</p>
      <span class="btn-teal">整形外科について　›</span>
    </article>
    <article class="dept-card">
      <div class="photo" role="img" aria-label="カルテを持つ医師と看護師"></div>
      <h3>総合内科</h3>
      <p>総合内科についての簡単な紹介文が入ります。風邪や生活習慣病など幅広く診療いたします。</p>
      <span class="btn-teal">総合内科について　›</span>
    </article>
    <article class="dept-card">
      <div class="photo" role="img" aria-label="歯科治療中の診察室"></div>
      <h3>歯科</h3>
      <p>歯科についての簡単な紹介文が入ります。虫歯治療から予防歯科まで丁寧に対応いたします。</p>
      <span class="btn-teal">歯科について　›</span>
    </article>
  </div>
</section>

<section class="banners">
  <a class="banner"><div class="photo" role="img" aria-label="働くスタッフの様子"></div><strong>採用情報</strong></a>
  <a class="banner"><div class="photo" role="img" aria-label="医師の紹介写真"></div><strong>クリニック紹介</strong></a>
  <a class="banner"><div class="photo" role="img" aria-label="受付での相談の様子"></div><strong>よくある質問</strong></a>
</section>

<div class="gallery">
  <div class="photo" role="img" aria-label="明るい診察室" style="background:linear-gradient(135deg,#eaf1ef,#cfe1dd)"></div>
  <div class="photo" role="img" aria-label="黄色い花" style="background:linear-gradient(135deg,#f4d56a,#e7b93a)"></div>
  <div class="photo" role="img" aria-label="木目の待合室" style="background:linear-gradient(135deg,#e9dcc6,#c9b08a)"></div>
  <div class="photo" role="img" aria-label="キッズスペース" style="background:linear-gradient(135deg,#f3eef0,#bfe0ea)"></div>
</div>

<footer class="site-footer">
  <div class="footer-brand">
    <div class="brand-mark"></div>
    <div><div class="brand-name">見本クリニック</div><div class="brand-sub">内科・整形外科・歯科</div></div>
  </div>
  <div class="footer-info">
    <table class="hours">
      <thead><tr><th>診療時間</th><th>月</th><th>火</th><th>水</th><th>木</th><th>金</th><th>土</th><th>日</th></tr></thead>
      <tbody>
        <tr><td class="time">9:00〜12:30</td><td class="dot">●</td><td class="dot">●</td><td class="dot">●</td><td class="dot">●</td><td class="dot">●</td><td class="dot">●</td><td>／</td></tr>
        <tr><td class="time">14:00〜18:00</td><td class="dot">●</td><td class="dot">●</td><td class="dot">●</td><td class="dot">●</td><td class="dot">●</td><td>▲</td><td>／</td></tr>
      </tbody>
    </table>
    <div>
      <div class="footer-address">
        <p><svg width="14" height="14" viewBox="0 0 24 24" fill="#6b4a2c"><path d="M12 2a7 7 0 0 0-7 7c0 5 7 13 7 13s7-8 7-13a7 7 0 0 0-7-7zm0 9.5A2.5 2.5 0 1 1 12 6.5a2.5 2.5 0 0 1 0 5z"/></svg>〒000-0000 見本県見本市中央1丁目2番3号</p>
        <p>見本中央駅より徒歩3分</p>
      </div>
      <div class="contact" style="position:static">
        <div class="tels">
          <div class="tel">010-234-5678</div>
          <div class="tel brown">010-234-5678</div>
        </div>
        <div class="reserve">予約</div>
      </div>
    </div>
  </div>
  <p class="footer-access">【交通機関】見本線「見本中央駅」より徒歩3分／見本バス「中央一丁目」停留所すぐ／お車でお越しの方は提携駐車場をご利用ください。駐輪場あり。</p>
</footer>

<nav class="footer-nav">
  <span>HOME</span><span>病院案内</span><span>ご挨拶・理念</span><span>施設案内</span><span>ドクター紹介</span><span>診療科目</span><span>アクセス</span><span>よくある質問</span><span>採用情報</span><span>サイトマップ</span><span>お問い合わせ</span>
</nav>

<div class="map photo" role="img" aria-label="クリニック周辺の地図"></div>
<div class="copyright">Copyright © 2017 MIHON CLINIC. All Rights Reserved.</div>
</body>
</html>
```